Icecream Label Design [Corla Bright]

Our company distributes ice cream in Japan. We produce a private brand that has always been know as Corlas.

However the brand design is poor and we have poor/almost zero brand recognition in the market. Currently people buy our product because it is made in NEW ZEALAND (quality) and represents very good value for money.

BUT

Going forward we want to market Corlas as a 'HIGH QUALITY' icecream BRAND in Japan. We need a package label that reflects this.

We are expanding the current product range (flavour and size) of our Corla's icecream.

I think this is a great opportunity to get your design exposed in a large Asian market. We have very good distribution channels and will will sell a lot of this ice cream in Japan in the future and the Corlas brand/logo will become well recognized.

Really looking forward to seeing design proposals! Thank you, any questions please ask - MTW

Reason: Good morning all. Thank you for submissions. We are wishing to see more examples so have decided to extend the deadline. Looking forward to seeing your ideas. Thanks! Declan

Hi All,

I have sent through the current Corla's logo. Please feel free to use this logo in your designs if you think it is appropriate. There is also an image of the current label for your reference - emphasis on fresh milk but the overall design is not good hence my request to you all...

Looking forward to your help and further submissions. 

Thanks!

Declan 

Reason: Just finalizing design. Have extended deadline to accommodate this. Your continued support and cooperation appreciated. Thanks! Declan

Reason: Finalizing decision being made. Thanks! Declan

Reason: Will make decision today. Thanks all! Declan

Target Market(s)

Mother's 30-55 (quality ingredients and value for money)

Industry/Entity Type

It Company

Requirements
Must have
• 1. The brand is Corla Bright

2. You are designing a logo that will be used on our 1 litre tub and 500ML pottle. Design specification files are attached*.
*Please note: on both the 1L and 500ML tub space must be left for regulatory information. Image attached showing current regulatory information and and space on the 1L tub.

3. We want to use this logo/branding as a base for all our 4 flavour varieties noted below so the design must be able to accommodate this somehow.

4. Needs to have a text placeholder for Japanese translation. ie: if on the design you use text that says 'Vanilla Ice Cream' then somewhere there needs to be space for the Japanese equivalent バニラ アイスクリーム
Nice to have
• 1. Corlas uses 100% fresh milk and cream. It would be nice to convey this somehow.

2. Perhaps could include text 'Your Fresh Taste of New Zealand'

3. There are 4* flavour varieties.
Vanilla | Strawberry | Chocolate | Green Tea
* it would be nice to have a good Corlas base design/pattern which can then be modified slightly (image, colour etc maybe) to reflect each unique flavour.

```html
<!DOCTYPE html>
<html lang="en">
<head>
<meta charset="utf-8">
<title>Corla's Ice Cream Labels</title>
<link rel="stylesheet" href="https://fonts.googleapis.com/css2?family=Cinzel:wght@400;700&family=Noto+Sans+JP:wght@400;500&display=swap">
<style>
  :root {
    --navy: #2b2a6e;
    --navy-light: #5a57a8;
    --white: #ffffff;
    --serif: 'Cinzel', 'Times New Roman', serif;
    --jp: 'Noto Sans JP', sans-serif;
  }
  html, body {
    margin: 0;
    padding: 0;
    width: 1200px;
    height: 900px;
    overflow: hidden;
    background: var(--white);
  }
  .sheet { position: relative; width: 1200px; height: 900px; }
  .label { position: absolute; width: 572px; height: 410px; }
  .label--green      { left: 12px;  top: 30px;
    --light: #9bcf5f; --dark: #176b35; --ink: #1f3f1f; --badge: #1b6b35; --badge-ink: #ffffff; --scoop-a: #cfe7a4; --scoop-b: #4f8f3a; --ring: #2f6e2c; }
  .label--strawberry { left: 604px; top: 30px;
    --light: #f2bcc4; --dark: #ef7aa0; --ink: #4a2430; --badge: #ef7aa0; --badge-ink: #ffffff; --scoop-a: #fbe1e6; --scoop-b: #d9476a; --ring: #c9607e; }
  .label--vanilla    { left: 12px;  top: 460px;
    --light: #e8cf7e; --dark: #c8972e; --ink: #3f2d0c; --badge: #f4e4a8; --badge-ink: #6b4a12; --scoop-a: #fbf0c8; --scoop-b: #c9a048; --ring: #a9802a; }
  .label--chocolate  { left: 604px; top: 460px;
    --light: #c49a6c; --dark: #3b2416; --ink: #2a170d; --badge: #3b2416; --badge-ink: #ffffff; --scoop-a: #b07a4c; --scoop-b: #3e2212; --ring: #4a2c18; }

  .label svg { display: block; width: 572px; height: 410px; }
  .field-light { fill: var(--light); }
  .field-dark  { fill: var(--dark); }
  .banner      { fill: var(--navy); }
  .banner-edge { fill: none; stroke: var(--navy-light); stroke-width: 4; }
  .brand-name  { font-family: var(--serif); font-weight: 700; font-size: 36px; fill: var(--white); }
  .brand-tag   { font-family: var(--serif); font-weight: 700; font-size: 12px; fill: var(--white); letter-spacing: 0.3px; }
  .badge       { fill: var(--badge); stroke: var(--white); stroke-width: 2; }
  .badge-big   { font-family: var(--serif); font-weight: 700; font-size: 19px; fill: var(--badge-ink); }
  .badge-small { font-family: var(--serif); font-weight: 700; font-size: 10px; fill: var(--badge-ink); }
  .scoop-ring  { fill: none; stroke: var(--ring); stroke-width: 3; }
  .flavour     { font-family: var(--serif); font-weight: 400; font-size: 20px; fill: var(--ink); letter-spacing: 1px; }
  .flavour-jp  { font-family: var(--jp); font-weight: 400; font-size: 14px; fill: var(--ink); }
  .tagline     { font-family: var(--serif); font-weight: 400; font-size: 17px; fill: var(--navy); }
</style>
</head>
<body>
<main class="sheet">

  <section class="label label--green">
    <svg viewBox="0 0 572 410" aria-labelledby="green-title">
      <title id="green-title">Corla's Green Tea Ice-Cream label</title>
      <defs>
        <radialGradient id="green-scoop" cx="50%" cy="40%" r="60%">
          <stop offset="0%" style="stop-color:var(--scoop-a)"/>
          <stop offset="100%" style="stop-color:var(--scoop-b)"/>
        </radialGradient>
        <linearGradient id="green-milk" x1="0" y1="0" x2="0" y2="1">
          <stop offset="0%" stop-color="#ffffff"/><stop offset="100%" stop-color="#ffffff" stop-opacity="0.6"/>
        </linearGradient>
        <path id="green-arc" d="M127.3 287 A84 84 0 1 1 272.7 287"/>
      </defs>
      <rect class="field-light" x="0" y="0" width="412" height="410"/>
      <rect class="field-dark" x="412" y="0" width="160" height="410"/>
      <path class="banner" d="M0 0 H310 C300 60 260 95 180 110 C110 125 50 130 0 146 Z"/>
      <path class="banner-edge" d="M0 153 C50 137 110 132 180 117 C262 102 304 66 316 2"/>
      <text class="brand-name" x="22" y="48">Corla's</text>
      <text class="brand-tag" x="24" y="74">High Quality Ice Cream</text>
      <rect x="310" y="0" width="96" height="120" rx="40" fill="url(#green-milk)" role="img" aria-label="Splash of fresh milk pouring"/>
      <circle class="badge" cx="372" cy="168" r="44"/>
      <text class="badge-big" x="372" y="162" text-anchor="middle">100%</text>
      <text class="badge-small" x="372" y="178" text-anchor="middle">FRESH MILK</text>
      <text class="badge-small" x="372" y="191" text-anchor="middle">&amp; CREAM</text>
      <circle cx="200" cy="245" r="72" fill="url(#green-scoop)" role="img" aria-label="Swirl of green tea ice cream with tea leaves"/>
      <circle class="scoop-ring" cx="200" cy="245" r="74"/>
      <text class="flavour"><textPath href="#green-arc" startOffset="50%" text-anchor="middle">GREEN TEA ICE-CREAM</textPath></text>
      <text class="flavour-jp" x="226" y="344" text-anchor="middle">抹茶　アイスクリーム</text>
      <text class="tagline" x="40" y="388">Your Fresh Taste of New Zealand.</text>
    </svg>
  </section>

  <section class="label label--strawberry">
    <svg viewBox="0 0 572 410" aria-labelledby="straw-title">
      <title id="straw-title">Corla's Strawberry Ice-Cream label</title>
      <defs>
        <radialGradient id="straw-scoop" cx="50%" cy="40%" r="60%">
          <stop offset="0%" style="stop-color:var(--scoop-a)"/>
          <stop offset="100%" style="stop-color:var(--scoop-b)"/>
        </radialGradient>
        <linearGradient id="straw-milk" x1="0" y1="0" x2="0" y2="1">
          <stop offset="0%" stop-color="#ffffff"/><stop offset="100%" stop-color="#ffffff" stop-opacity="0.6"/>
        </linearGradient>
        <path id="straw-arc" d="M127.3 287 A84 84 0 1 1 272.7 287"/>
      </defs>
      <rect class="field-light" x="0" y="0" width="412" height="410"/>
      <rect class="field-dark" x="412" y="0" width="160" height="410"/>
      <path class="banner" d="M0 0 H310 C300 60 260 95 180 110 C110 125 50 130 0 146 Z"/>
      <path class="banner-edge" d="M0 153 C50 137 110 132 180 117 C262 102 304 66 316 2"/>
      <text class="brand-name" x="22" y="48">Corla's</text>
      <text class="brand-tag" x="24" y="74">High Quality Ice Cream</text>
      <rect x="310" y="0" width="96" height="120" rx="40" fill="url(#straw-milk)" role="img" aria-label="Splash of fresh milk pouring"/>
      <circle class="badge" cx="372" cy="168" r="44"/>
      <text class="badge-big" x="372" y="162" text-anchor="middle">100%</text>
      <text class="badge-small" x="372" y="178" text-anchor="middle">FRESH MILK</text>
      <text class="badge-small" x="372" y="191" text-anchor="middle">&amp; CREAM</text>
      <circle cx="200" cy="245" r="72" fill="url(#straw-scoop)" role="img" aria-label="Swirl of strawberry ice cream with a fresh strawberry"/>
      <circle class="scoop-ring" cx="200" cy="245" r="74"/>
      <text class="flavour"><textPath href="#straw-arc" startOffset="50%" text-anchor="middle">STRAWBERRY ICE-CREAM</textPath></text>
      <text class="flavour-jp" x="226" y="344" text-anchor="middle">ストロベリーアイスクリーム</text>
      <text class="tagline" x="40" y="388">Your Fresh Taste of New Zealand.</text>
    </svg>
  </section>

  <section class="label label--vanilla">
    <svg viewBox="0 0 572 410" aria-labelledby="van-title">
      <title id="van-title">Corla's Vanilla Ice-Cream label</title>
      <defs>
        <radialGradient id="van-scoop" cx="50%" cy="40%" r="60%">
          <stop offset="0%" style="stop-color:var(--scoop-a)"/>
          <stop offset="100%" style="stop-color:var(--scoop-b)"/>
        </radialGradient>
        <linearGradient id="van-milk" x1="0" y1="0" x2="0" y2="1">
          <stop offset="0%" stop-color="#ffffff"/><stop offset="100%" stop-color="#ffffff" stop-opacity="0.6"/>
        </linearGradient>
        <path id="van-arc" d="M127.3 287 A84 84 0 1 1 272.7 287"/>
      </defs>
      <rect class="field-light" x="0" y="0" width="412" height="410"/>
      <rect class="field-dark" x="412" y="0" width="160" height="410"/>
      <path class="banner" d="M0 0 H310 C300 60 260 95 180 110 C110 125 50 130 0 146 Z"/>
      <path class="banner-edge" d="M0 153 C50 137 110 132 180 117 C262 102 304 66 316 2"/>
      <text class="brand-name" x="22" y="48">Corla's</text>
      <text class="brand-tag" x="24" y="74">High Quality Ice Cream</text>
      <rect x="310" y="0" width="96" height="120" rx="40" fill="url(#van-milk)" role="img" aria-label="Splash of fresh milk pouring"/>
      <circle class="badge" cx="372" cy="168" r="44"/>
      <text class="badge-big" x="372" y="162" text-anchor="middle">100%</text>
      <text class="badge-small" x="372" y="178" text-anchor="middle">FRESH MILK</text>
      <text class="badge-small" x="372" y="191" text-anchor="middle">&amp; CREAM</text>
      <circle cx="200" cy="245" r="72" fill="url(#van-scoop)" role="img" aria-label="Swirl of vanilla ice cream with vanilla pods and flower"/>
      <circle class="scoop-ring" cx="200" cy="245" r="74"/>
      <text class="flavour"><textPath href="#van-arc" startOffset="50%" text-anchor="middle">VANILLA ICE-CREAM</textPath></text>
      <text class="flavour-jp" x="226" y="344" text-anchor="middle">バニラ　アイスクリーム</text>
      <text class="tagline" x="40" y="388">Your Fresh Taste of New Zealand.</text>
    </svg>
  </section>

  <section class="label label--chocolate">
    <svg viewBox="0 0 572 410" aria-labelledby="choc-title">
      <title id="choc-title">Corla's Chocolate Ice-Cream label</title>
      <defs>
        <radialGradient id="choc-scoop" cx="50%" cy="40%" r="60%">
          <stop offset="0%" style="stop-color:var(--scoop-a)"/>
          <stop offset="100%" style="stop-color:var(--scoop-b)"/>
        </radialGradient>
        <linearGradient id="choc-milk" x1="0" y1="0" x2="0" y2="1">
          <stop offset="0%" stop-color="#ffffff"/><stop offset="100%" stop-color="#ffffff" stop-opacity="0.6"/>
        </linearGradient>
        <path id="choc-arc" d="M127.3 287 A84 84 0 1 1 272.7 287"/>
      </defs>
      <rect class="field-light" x="0" y="0" width="412" height="410"/>
      <rect class="field-dark" x="412" y="0" width="160" height="410"/>
      <path class="banner" d="M0 0 H310 C300 60 260 95 180 110 C110 125 50 130 0 146 Z"/>
      <path class="banner-edge" d="M0 153 C50 137 110 132 180 117 C262 102 304 66 316 2"/>
      <text class="brand-name" x="22" y="48">Corla's</text>
      <text class="brand-tag" x="24" y="74">High Quality Ice Cream</text>
      <rect x="310" y="0" width="96" height="120" rx="40" fill="url(#choc-milk)" role="img" aria-label="Splash of fresh milk pouring"/>
      <circle class="badge" cx="372" cy="168" r="44"/>
      <text class="badge-big" x="372" y="162" text-anchor="middle">100%</text>
      <text class="badge-small" x="372" y="178" text-anchor="middle">FRESH MILK</text>
      <text class="badge-small" x="372" y="191" text-anchor="middle">&amp; CREAM</text>
      <circle cx="200" cy="245" r="72" fill="url(#choc-scoop)" role="img" aria-label="Swirl of chocolate ice cream with chocolate pieces"/>
      <circle class="scoop-ring" cx="200" cy="245" r="74"/>
      <text class="flavour"><textPath href="#choc-arc" startOffset="50%" text-anchor="middle">CHOCOLATE ICE-CREAM</textPath></text>
      <text class="flavour-jp" x="226" y="344" text-anchor="middle">チョコレートアイスクリーム</text>
      <text class="tagline" x="40" y="388">Your Fresh Taste of New Zealand.</text>
    </svg>
  </section>

</main>
</body>
</html>
```